Plakate für Podologie - Medizinische Fusspflege
Zielgruppe
Podologie - Medizinische Fusspflege. Zielgruppe sind Kinder bis und mit ältere Menschen.
Aufgabenstellung
Möchte ein modernes, aber auch klassisches Design, dass Professionalität & medizinische Fundiertheit ausstrahlt. Man soll sehen, dass es medizinisch ist und nicht verwechselbar mit kosmetischer Fusspflege.

```html
<!DOCTYPE html>
<html lang="de">
<head>
<meta charset="utf-8">
<title>Pedalis – Medizinische Podologie</title>
<link rel="stylesheet" href="https://fonts.googleapis.com/css2?family=Open+Sans:wdth,wght@75..100,400..800&display=swap">
<style>
  :root {
    --teal: #145a55;
    --green: #6aad45;
    --grey-text: #4a4f52;
    --white: #ffffff;
    --page-bg: #d2d2d2;
    --skin: #f2c7a6;
    --lilac: #a58fc8;
    --icon-ring: #dfe7e6;
  }
  * { margin: 0; padding: 0; box-sizing: border-box; }
  html, body { width: 1000px; height: 1200px; overflow: hidden; background: var(--page-bg); }
  body { font-family: "Open Sans", Arial, sans-serif; font-stretch: 87.5%; }

  .poster {
    position: absolute; left: 90px; top: 20px; width: 820px; height: 1160px;
    background: var(--white); overflow: hidden;
  }
  .hero-photo {
    position: absolute; left: 440px; top: 80px; width: 380px; height: 720px;
    background:
      radial-gradient(ellipse 50% 48% at 62% 48%, var(--skin) 0%, rgba(242,199,166,0.65) 55%, rgba(242,199,166,0) 100%),
      linear-gradient(160deg, rgba(165,143,200,0.55) 0%, rgba(220,210,235,0.3) 45%, rgba(255,255,255,0) 90%);
    -webkit-mask-image: linear-gradient(90deg, transparent 0%, #000 30%);
    mask-image: linear-gradient(90deg, transparent 0%, #000 30%);
  }
  .waves { position: absolute; inset: 0; }

  .brand { position: absolute; left: 48px; top: 40px; }
  .brand-row { display: flex; align-items: center; gap: 14px; }
  .brand-dot { width: 58px; height: 58px; border-radius: 50%; background: var(--teal); }
  .brand-name { font-size: 48px; font-weight: 600; color: var(--teal); line-height: 1; }
  .brand-tagline { margin: 10px 0 0 72px; font-size: 14px; letter-spacing: 2.4px; color: var(--grey-text); font-stretch: 100%; }

  .headline {
    position: absolute; left: 42px; top: 198px; font-size: 58px; line-height: 54px;
    font-weight: 800; color: var(--teal); font-stretch: 75%;
  }
  .subline {
    position: absolute; left: 46px; top: 334px; font-size: 32px; line-height: 35px;
    color: var(--grey-text); font-stretch: 80%;
  }
  .subline-rule { position: absolute; left: 48px; top: 416px; width: 135px; height: 2px; background: var(--green); }

  .services { position: absolute; left: 50px; top: 460px; list-style: none; }
  .service { display: flex; align-items: center; height: 60px; margin-bottom: 14px; }
  .service-icon { width: 60px; height: 60px; flex: none; }
  .service-label { margin-left: 14px; font-size: 25px; color: var(--teal); font-stretch: 80%; }

  .cta {
    position: absolute; left: 491px; top: 740px; width: 212px; height: 212px; border-radius: 50%;
    background: var(--teal); border: 6px solid var(--white);
    display: flex; flex-direction: column; align-items: center; justify-content: center;
    color: var(--white); font-weight: 600; font-size: 38px; line-height: 40px; text-align: center; font-stretch: 75%;
  }
  .cta::after { content: ""; width: 100px; height: 2px; background: var(--green); margin-top: 6px; }

  .contact { position: absolute; left: 50px; top: 965px; list-style: none; color: var(--white); }
  .contact-item { display: flex; align-items: center; height: 44px; margin-bottom: 16px; font-size: 22px; line-height: 24px; font-stretch: 80%; }
  .contact-icon { width: 44px; height: 44px; flex: none; margin-right: 16px; }

  .divider { position: absolute; left: 380px; top: 986px; width: 2px; height: 150px; background: var(--green); }

  .certified { position: absolute; left: 420px; top: 996px; display: flex; color: var(--white); font-stretch: 80%; }
  .certified-badge { width: 62px; height: 62px; flex: none; margin-top: 30px; margin-right: 24px; }
  .certified-title { font-size: 28px; font-weight: 600; line-height: 34px; }
  .certified-text { font-size: 23px; line-height: 29px; margin-top: 6px; }
</style>
</head>
<body>
<main class="poster">
  <div class="hero-photo" role="img" aria-label="Foto: Hände in medizinischen Handschuhen behandeln eine Fusssohle"></div>

  <svg class="waves" viewBox="0 0 820 1160" aria-hidden="true">
    <defs>
      <linearGradient id="band-green" x1="0" x2="1" y1="0" y2="0">
        <stop offset="0" stop-color="#6aad45"/>
        <stop offset="0.5" stop-color="#eef4e4"/>
        <stop offset="0.75" stop-color="#8cc063"/>
        <stop offset="1" stop-color="#2a8a6e"/>
      </linearGradient>
    </defs>
    <path d="M0,845 Q400,965 820,790 L820,890 Q400,990 0,896 Z" fill="url(#band-green)"/>
    <path d="M0,896 Q400,990 820,890 L820,1160 L0,1160 Z" fill="#145a55"/>
  </svg>

  <header class="brand">
    <div class="brand-row">
      <span class="brand-dot"></span>
      <span class="brand-name">Pedalis</span>
    </div>
    <p class="brand-tagline">MEDIZINISCHE PODOLOGIE</p>
  </header>

  <h1 class="headline">IHRE FÜSSE.<br>UNSERE KOMPETENZ.</h1>
  <p class="subline">Medizinische Fussbehandlungen<br>für Ihre Gesundheit und Lebensqualität.</p>
  <div class="subline-rule"></div>

  <ul class="services">
    <li class="service">
      <svg class="service-icon" viewBox="0 0 60 60"><circle cx="30" cy="30" r="28" fill="none" stroke="#dfe7e6" stroke-width="2"/><path d="M24 18 Q20 32 28 40" fill="none" stroke="#145a55" stroke-width="2"/><path d="M38 28v10M33 33h10" stroke="#6aad45" stroke-width="2.5"/></svg>
      <span class="service-label">Medizinische Fusspflege</span>
    </li>
    <li class="service">
      <svg class="service-icon" viewBox="0 0 60 60"><circle cx="30" cy="30" r="28" fill="none" stroke="#dfe7e6" stroke-width="2"/><path d="M20 44V26a6 6 0 0 1 12 0v18M34 44V33a4 4 0 0 1 8 0v11" fill="none" stroke="#145a55" stroke-width="2"/></svg>
      <span class="service-label">Nagelkorrektur</span>
    </li>
    <li class="service">
      <svg class="service-icon" viewBox="0 0 60 60"><circle cx="30" cy="30" r="28" fill="none" stroke="#dfe7e6" stroke-width="2"/><path d="M22 44V26a8 8 0 0 1 16 0v18M25 34h10" fill="none" stroke="#145a55" stroke-width="2"/><path d="M42 22l4-3M43 28h4" stroke="#6aad45" stroke-width="2"/></svg>
      <span class="service-label">Eingewachsene Nägel</span>
    </li>
    <li class="service">
      <svg class="service-icon" viewBox="0 0 60 60"><circle cx="30" cy="30" r="28" fill="none" stroke="#dfe7e6" stroke-width="2"/><path d="M22 20 Q20 36 26 46 M38 20 Q40 36 34 46" fill="none" stroke="#145a55" stroke-width="2"/><circle cx="30" cy="30" r="3" fill="#6aad45"/></svg>
      <span class="service-label">Hornhaut &amp; Hühneraugen</span>
    </li>
    <li class="service">
      <svg class="service-icon" viewBox="0 0 60 60"><circle cx="30" cy="30" r="28" fill="none" stroke="#dfe7e6" stroke-width="2"/><path d="M30 15l12 5v9c0 8-5 13-12 16-7-3-12-8-12-16v-9z" fill="none" stroke="#145a55" stroke-width="2"/><path d="M30 24v12M24 30h12" stroke="#6aad45" stroke-width="3"/></svg>
      <span class="service-label">Diabetische Fussversorgung</span>
    </li>
  </ul>

  <div class="cta">JETZT<br>TERMIN<br>SICHERN!</div>

  <ul class="contact">
    <li class="contact-item">
      <svg class="contact-icon" viewBox="0 0 44 44"><circle cx="22" cy="22" r="21" fill="#fff"/><path d="M15 13l5 0 2 6-3 2c1 3 3 5 6 6l2-3 6 2v5c-10 1-19-8-18-18z" fill="none" stroke="#145a55" stroke-width="2"/></svg>
      0471 / 238 615 0
    </li>
    <li class="contact-item">
      <svg class="contact-icon" viewBox="0 0 44 44"><circle cx="22" cy="22" r="21" fill="#fff"/><circle cx="22" cy="22" r="11" fill="none" stroke="#145a55" stroke-width="2"/><ellipse cx="22" cy="22" rx="5" ry="11" fill="none" stroke="#145a55" stroke-width="2"/><path d="M11 22h22M13 16h18M13 28h18" stroke="#145a55" stroke-width="1.5"/></svg>
      www.pedalis-praxis.de
    </li>
    <li class="contact-item">
      <svg class="contact-icon" viewBox="0 0 44 44"><circle cx="22" cy="22" r="21" fill="#fff"/><path d="M22 33s-7-8-7-13a7 7 0 0 1 14 0c0 5-7 13-7 13z" fill="none" stroke="#145a55" stroke-width="2"/><circle cx="22" cy="20" r="2.5" fill="#145a55"/></svg>
      <span>Lindenweg 14<br>48231 Talbrück</span>
    </li>
  </ul>

  <div class="divider"></div>

  <section class="certified">
    <svg class="certified-badge" viewBox="0 0 62 62"><circle cx="31" cy="27" r="24" fill="none" stroke="#6aad45" stroke-width="2"/><circle cx="31" cy="27" r="12" fill="#6aad45"/><path d="M25 27l4 4 8-8" fill="none" stroke="#fff" stroke-width="2.5"/></svg>
    <div>
      <h2 class="certified-title">Zertifizierte Podologen</h2>
      <p class="certified-text">Fachgerechte, hygienische<br>und moderne Behandlung<br>auf medizinischem Niveau.</p>
    </div>
  </section>
</main>
</body>
</html>
```